KESTREL Communications Business Card- Belsa

Kestrel Integrated Communications is Corporate communications agency with more than 20 years of experience. We become part of the manegement team of our clients in other to improve their outcomes and grow the possitioning of their brand.
We are in Puerto Rico, latin caribbean island
Name: Maribelsa (Belsa) Ocampo
787-555-0148
bocampo@kestrelwing.example

Target Market(s)

finance and pharmaceutical companies

Industry/Entity Type

Business

Contact Information for Business Card

modern, edgy colorful and playfull like our logo

Requirements
Must have
• company logo
• name
• tel
• email

```html
<!DOCTYPE html>
<html lang="en">
<head>
<meta charset="utf-8">
<title>Kestrel Integrated Communications – Business Card</title>
<link rel="stylesheet" href="https://fonts.googleapis.com/css2?family=Tinos:wght@400;700&display=swap">
<style>
  :root {
    --orange: #f05a22;
    --brown: #3a2c17;
    --white: #ffffff;
    --backdrop: #e4e4e6;
    --serif: "Tinos", "Times New Roman", serif;
  }
  * { box-sizing: border-box; margin: 0; padding: 0; }
  html, body { width: 1200px; height: 800px; overflow: hidden; }
  body {
    background: var(--backdrop);
    font-family: var(--serif);
    position: relative;
  }
  .card {
    position: absolute;
    top: 250px;
    width: 525px;
    height: 300px;
    overflow: hidden;
    box-shadow: 0 6px 18px rgba(0,0,0,0.18);
  }
  .card--front { left: 50px; }
  .card--back { left: 625px; background: var(--white); }

  .front-art { position: absolute; inset: 0; }
  .front-wordmark {
    position: absolute;
    left: 50%; top: 50%;
    transform: translate(-50%, -50%) rotate(-28deg);
    text-align: center;
    color: var(--brown);
    font-weight: 700;
    font-size: 30px;
    line-height: 1.1;
    letter-spacing: 1px;
    white-space: nowrap;
  }
  .front-wordmark small { display: block; font-size: 15px; letter-spacing: 2px; }

  .band { position: absolute; left: 0; right: 0; }
  .band--top { top: 0; height: 38px; background: var(--orange); }
  .band--bottom { bottom: 0; height: 72px; background: var(--brown); }

  .back-wordmark {
    position: absolute;
    left: 230px; top: 138px;
    transform: translateX(-50%);
    text-align: center;
    color: var(--brown);
    font-weight: 700;
    font-size: 26px;
    line-height: 1.1;
    letter-spacing: 1px;
    white-space: nowrap;
  }
  .back-wordmark small { display: block; font-size: 10px; letter-spacing: 1.5px; }

  .contact { position: absolute; font-size: 12px; line-height: 1.3; white-space: nowrap; }
  .contact .name { font-weight: 700; font-size: 17px; margin-bottom: 10px; }
  .contact--main { left: 340px; top: 108px; color: var(--brown); }
  .contact--flipped {
    left: 22px; top: 50px;
    color: var(--orange);
    transform: rotate(180deg);
    text-align: right;
  }
</style>
</head>
<body>
  <section class="card card--front" aria-label="Business card front">
    <svg class="front-art" viewBox="0 0 525 300" width="525" height="300" aria-hidden="true">
      <polygon points="0,0 300,0 225,300 0,300" fill="var(--orange)"/>
      <polygon points="300,0 525,0 525,300 225,300" fill="var(--brown)"/>
      <ellipse cx="262" cy="150" rx="230" ry="120" transform="rotate(-28 262 150)" fill="var(--white)"/>
    </svg>
    <div class="front-wordmark">KESTREL<small>INTEGRATED COMMUNICATIONS</small></div>
  </section>

  <section class="card card--back" aria-label="Business card back">
    <div class="band band--top"></div>
    <div class="band band--bottom"></div>

    <div class="contact contact--flipped">
      <p class="name">Maribelsa Ocampo</p>
      <p>787-555-0148</p>
      <p>bocampo@kestrelwing.example</p>
    </div>

    <div class="back-wordmark">KESTREL<small>INTEGRATED COMMUNICATIONS</small></div>

    <div class="contact contact--main">
      <p class="name">Maribelsa Ocampo</p>
      <p>787-555-0148</p>
      <p>bocampo@kestrelwing.example</p>
    </div>
  </section>
</body>
</html>
```